Harborline Stay Collective Business Card Design

Design a business card for Harborline Stay Collective. Look at the website for colors and reference. Card should have logo, name, title, office number, mobile number, email, URL and a tagline like, "Luxury Hotel & Resort Email Marketing" (This might change).

https://www.harborlinestaycollective.net

The rest I will leave up to your imagination.

Contact Information for Business Card

Logo, name, title, office number, mobile number, email, URL and a tagline like, "Luxury Hotel & Resort Email Marketing" (This might change).

```html
<!DOCTYPE html>
<html lang="en">
<head>
<meta charset="utf-8">
<title>Harborline Stay Collective — Business Card</title>
<link rel="stylesheet" href="https://fonts.googleapis.com/css2?family=Montserrat:wght@400;500;600;700&display=swap">
<style>
  :root {
    --stage: #3b3b3b;
    --card: #1f1f1f;
    --card-light: #2a2a2a;
    --accent: #f07a16;
    --ink: #ffffff;
    --ink-soft: #e6e6e6;
  }
  * { box-sizing: border-box; margin: 0; padding: 0; }
  html, body { width: 1200px; height: 987px; overflow: hidden; }
  body {
    background: var(--stage);
    font-family: "Montserrat", sans-serif;
    position: relative;
  }
  .card {
    position: absolute;
    width: 620px;
    height: 354px;
    background: radial-gradient(ellipse at 40% 40%, var(--card-light), var(--card) 75%);
    border-bottom: 4px solid var(--accent);
    box-shadow: 0 14px 40px rgba(0,0,0,.45);
  }
  .card-front { left: 150px; top: 100px; }
  .card-back { left: 430px; top: 530px; }

  .wordmark {
    display: flex;
    align-items: center;
    gap: 14px;
    color: var(--ink);
    font-weight: 700;
    text-transform: uppercase;
    letter-spacing: .04em;
    line-height: 1.1;
  }
  .wordmark-square {
    flex: none;
    background: var(--accent);
  }

  .card-front .wordmark {
    position: absolute;
    left: 0; right: 0; top: 120px;
    justify-content: center;
    font-size: 34px;
  }
  .card-front .wordmark-square { width: 22px; height: 22px; }
  .tagline {
    position: absolute;
    left: 0; right: 0; top: 250px;
    text-align: center;
    color: var(--ink);
    font-size: 16px;
    font-weight: 500;
  }
  .tagline .amp { color: var(--accent); }

  .card-back .wordmark {
    position: absolute;
    left: 34px; top: 150px;
    width: 300px;
    font-size: 22px;
  }
  .card-back .wordmark-square { width: 16px; height: 16px; }
  .divider {
    position: absolute;
    left: 352px; top: 70px;
    width: 2px; height: 150px;
    background: var(--accent);
  }
  .contact {
    position: absolute;
    left: 376px; top: 62px;
    right: 14px;
  }
  .contact-name {
    color: var(--accent);
    font-size: 22px;
    font-weight: 700;
  }
  .contact-title {
    color: var(--ink);
    font-size: 14px;
    font-weight: 500;
    margin-bottom: 18px;
  }
  .contact-list { list-style: none; }
  .contact-list li {
    display: flex;
    align-items: center;
    gap: 8px;
    color: var(--ink-soft);
    font-size: 11.5px;
    line-height: 1.75;
    white-space: nowrap;
  }
  .contact-list svg { width: 12px; height: 12px; flex: none; }
</style>
</head>
<body>

<section class="card card-front">
  <div class="wordmark"><span class="wordmark-square"></span><span>Harborline Stay Collective</span></div>
  <p class="tagline">Luxury Hotel <span class="amp">&amp;</span> Resort Email Marketing</p>
</section>

<section class="card card-back">
  <div class="wordmark"><span class="wordmark-square"></span><span>Harborline Stay Collective</span></div>
  <div class="divider"></div>
  <div class="contact">
    <h2 class="contact-name">Daniel Reeve</h2>
    <p class="contact-title">Managing Director</p>
    <ul class="contact-list">
      <li>
        <svg viewBox="0 0 24 24"><path fill="#f07a16" d="M6.6 10.8a15 15 0 0 0 6.6 6.6l2.2-2.2a1 1 0 0 1 1-.25 11.4 11.4 0 0 0 3.6.57 1 1 0 0 1 1 1V20a1 1 0 0 1-1 1A17 17 0 0 1 3 4a1 1 0 0 1 1-1h3.5a1 1 0 0 1 1 1c0 1.25.2 2.45.57 3.6a1 1 0 0 1-.25 1z"/></svg>
        555.204.6100
      </li>
      <li>
        <svg viewBox="0 0 24 24"><rect x="6" y="2" width="12" height="20" rx="2" fill="none" stroke="#f07a16" stroke-width="2"/><circle cx="12" cy="18" r="1.2" fill="#f07a16"/></svg>
        555.204.7315
      </li>
      <li>
        <svg viewBox="0 0 24 24"><rect x="2" y="5" width="20" height="14" fill="#f07a16"/><path d="M2 5l10 8 10-8" fill="none" stroke="#1f1f1f" stroke-width="2"/></svg>
        dreeve@harborlinestaycollective.net
      </li>
      <li>
        <svg viewBox="0 0 24 24" fill="none" stroke="#f07a16" stroke-width="2"><circle cx="12" cy="12" r="10"/><path d="M2 12h20M12 2c3 3 3 17 0 20M12 2c-3 3-3 17 0 20"/></svg>
        harborlinestaycollective.net
      </li>
    </ul>
  </div>
</section>

</body>
</html>
```